Brickline Gains Online Redesign

The company needs a new online presence built that better represents who we are and what we do. Our online presence needs to be optimised for both PC, tablet and Phone usage.

Our existing site; www.bricklinegains.com.au - this page currently forwards to one of our sales pages.
The entire site needs to be redesigned along with the sales pages /workshop and /faststart

Here are our competition:
https://www.coraltemsby.com/
http://quorvahomeschooling.com.au/property-education-experts/coral-temsby/
http://harrietvolonsky.com.au/
www.refitforyield.com.au/
http://fullmanualtorefurb.com.au/

Target Market(s)

40-55 Husband and Wife with children that are busy profesionals with a family income of 150-300k PA with 2-3 kids

Industry/Entity Type

Education

Number of Pages Required

5+ page

Font styles to use
Sans Serif
Script

Colors

Designer to choose colors to be used in the design.

Requirements
Must have
• Main Page
• Events Page
• Media Page
• Past Projects
• Blog - plesae design a template blog; both individual blogs and library (i like this http://bram.blog/)
• eBooks page
• Shopping Cart - buy eBooks, eBook Packs and courses
• eBook download page for each eBook
• Testimonials
• Event Sales Page
• 2 hr Event - currently www.bricklinegains.com.au/workshop & /faststart & /faststartv
Nice to have
• A few different options for sales landing pages to sell the 2 hr event
• A few different blog templates - video, text, infographic etc
• The business is a Property Educatiom, Mentoring and Consulting Company
Should not have
• This is not a real estate sales business

```html
<!DOCTYPE html>
<html lang="en">
<head>
<meta charset="utf-8">
<title>Brickline Gains – Renovating Property for Profit Workshop</title>
<link href="https://fonts.googleapis.com/css2?family=Lato:ital,wght@0,400;0,700;0,900;1,400&display=swap" rel="stylesheet">
<style>
:root{
  --navy:#0b1f55;
  --navy-deep:#08173f;
  --green:#2bb673;
  --orange:#f7931e;
  --ink:#1d2433;
  --text:#5b6272;
  --muted:#8a909c;
  --line:#d9dce2;
  --paper:#ffffff;
  --mist:#eef0f3;
  --foot:#f0f1f3;
}
*{box-sizing:border-box;margin:0;padding:0}
html,body{width:1200px;height:3536px;overflow:hidden}
body{font-family:'Lato',sans-serif;color:var(--ink);background:var(--paper);position:relative}
section,header,footer{position:absolute;left:0;width:1200px}
.btn{position:absolute;display:flex;align-items:center;justify-content:center;background:var(--green);color:#fff;font-size:12px;font-weight:700;letter-spacing:.5px;text-transform:uppercase}
.eyebrow{position:absolute;width:100%;text-align:center;color:var(--green);font-size:10px;font-weight:700;letter-spacing:1px;text-transform:uppercase}
.section-title{position:absolute;width:100%;text-align:center;font-size:24px;font-weight:700;color:var(--ink)}

/* hero */
.hero{top:0;height:560px}
.hero-photo{position:absolute;left:0;top:0;width:601px;height:560px;background:linear-gradient(160deg,#3b5578 0%,#2a3e5c 35%,#6a4a3e 62%,#3c4a2e 85%,#26311f 100%)}
.hero-panel{position:absolute;left:601px;top:0;width:599px;height:560px;background:var(--navy)}
.brand{position:absolute;display:flex;align-items:center;gap:8px;font-weight:900;letter-spacing:.5px;white-space:nowrap}
.brand-mark{width:14px;height:14px;background:var(--orange);flex:none}
.hero .brand{left:70px;top:46px;color:#fff;font-size:14px}
.main-nav{position:absolute;left:256px;top:49px;display:flex;gap:30px;color:#fff;font-size:13px;font-weight:700}
.ask{position:absolute;left:665px;top:48px;display:flex;align-items:center;gap:10px;color:#fff;font-size:12px;font-weight:700;letter-spacing:.5px}
.ask .num{font-size:16px}
.play{position:absolute;left:270px;top:248px}
.hero-title{position:absolute;left:662px;top:172px;width:420px;color:#fff;font-size:26px;font-weight:700;line-height:33px;text-transform:uppercase}
.hero-meta{position:absolute;left:662px;top:252px;color:#c9d0e3;font-size:12px;display:flex;align-items:center;gap:6px;white-space:nowrap}
.hero-tag{position:absolute;left:662px;top:298px;width:300px;color:#fff;font-size:15px;line-height:20px}
.hero-tag em{font-style:italic}
.hero-price{position:absolute;left:662px;top:372px;color:var(--orange);font-size:22px}
.hero-price b{font-weight:900}

/* instructors */
.instructors{top:560px;height:484px;background:var(--paper)}
.instructor{position:absolute;top:119px;width:420px;height:340px}
.instructor-photo{position:absolute;left:0;top:0;width:146px;height:146px;border-radius:50%;border:4px solid var(--navy);background:linear-gradient(180deg,#c9ced6,#8c96a6)}
.instructor-chart{position:absolute;left:150px;top:6px}
.instructor-name{position:absolute;left:2px;top:134px;width:194px;height:22px;background:var(--orange);color:#fff;font-size:14px;font-weight:700;padding-left:14px;line-height:22px}
.instructor-bio{position:absolute;left:19px;top:170px;width:370px;font-size:11.5px;line-height:19px;color:var(--text)}
.instructor .btn{left:19px;top:288px;width:80px;height:32px;background:var(--orange)}
.instructor.two .btn{background:var(--green)}

/* topics */
.topics{top:1044px;height:677px;background:var(--mist)}
.topics-sub{position:absolute;top:89px;width:100%;text-align:center;font-size:11px;color:var(--text)}
.topic-list{position:absolute;left:226px;top:130px;width:726px;list-style:none;border-top:1px solid var(--line)}
.topic{position:relative;height:40px;border-bottom:1px solid var(--line);display:flex;align-items:center;padding-left:12px;font-size:13px;color:var(--ink)}
.topic .no{color:var(--green);font-weight:700;margin-right:6px}
.topic .toggle{position:absolute;right:12px;top:15px;width:10px;height:10px;border-radius:50%;border:2px solid var(--muted)}
.topic.open{height:auto;display:block;padding:12px 0 16px 12px}
.topic.open .toggle{border-color:var(--green);background:var(--green)}
.topic-body{margin:18px 0 0 30px;width:640px;font-size:11.5px;line-height:17px;color:var(--text)}
.topic-body b{color:var(--ink);font-weight:700}
.topic-body p{margin-bottom:14px}

/* stories */
.stories{top:1721px;height:749px;background:var(--paper)}
.story{position:absolute;top:122px;width:280px;height:227px}
.story-photo{position:absolute;left:0;top:0;width:280px;height:149px}
.story-bar{position:absolute;left:0;top:149px;width:280px;height:78px;background:var(--navy);color:#fff}
.story-place{position:absolute;left:10px;top:-18px;font-size:11px;font-weight:700;color:#fff;text-transform:uppercase}
.story-figs{position:absolute;left:10px;top:22px;font-size:11px;font-weight:700;line-height:16px}
.story-badge{position:absolute;left:176px;top:-12px}
.carousel-arrow{position:absolute;top:227px}
.people-title{position:absolute;top:418px;width:100%;text-align:center;font-size:21px;font-weight:700}
.avatar{position:absolute;border-radius:50%;background:linear-gradient(180deg,#d8dce3,#9aa3b2)}
.quote{position:absolute;left:243px;top:575px;width:714px;text-align:center;font-size:13px;line-height:20px;color:var(--text)}
.quote .mark{color:var(--green);font-weight:900}
.quote-name{position:absolute;top:670px;width:100%;text-align:center;font-size:13px;color:var(--ink)}
.quote-date{position:absolute;top:690px;width:100%;text-align:center;font-size:10px;color:var(--muted)}

/* dates */
.dates{top:2470px;height:335px;background:var(--navy);color:#fff}
.dates-title{position:absolute;top:52px;width:100%;text-align:center;font-size:22px;font-weight:700}
.dates-table{position:absolute;left:156px;top:99px;width:888px;border-collapse:collapse;color:#fff}
.dates-table th{height:38px;font-size:11px;font-weight:700;text-transform:uppercase;letter-spacing:.5px;border-top:1px solid #2c3f74;border-bottom:1px solid #2c3f74}
.dates-table th+th,.dates-table td+td{border-left:1px solid #2c3f74}
.dates-table td{height:66px;text-align:center;font-size:15px;vertical-align:top;padding-top:18px}
.dates-table .map{display:block;font-size:11px;color:var(--green);margin-top:4px}
.dates-table .price{color:var(--orange);font-weight:700}
.th-in{display:inline-flex;align-items:center;gap:6px}

/* ebook */
.ebook{top:2805px;height:412px;background:var(--paper)}
.ebook-title{position:absolute;left:231px;top:88px;font-size:42px;color:var(--orange);line-height:46px}
.ebook-sub{position:absolute;left:231px;top:140px;width:240px;font-size:22px;line-height:30px;color:var(--ink)}
.ebook-note{position:absolute;left:231px;top:212px;width:230px;font-size:11px;line-height:16px;color:var(--text)}
.ebook .btn{left:231px;top:283px;width:160px;height:35px}
.cover{position:absolute;box-shadow:0 6px 14px rgba(0,0,0,.2)}

/* footer */
.site-footer{top:3217px;height:319px;background:var(--foot)}
.site-footer .brand{left:153px;top:62px;color:var(--navy);font-size:18px}
.foot-col{position:absolute;top:52px;font-size:11px;line-height:18px;color:var(--text)}
.foot-col h4{font-size:13px;color:var(--ink);font-weight:700;margin-bottom:6px}
.foot-col ul{list-style:none}
.foot-col .active{color:var(--orange)}
.foot-phone{display:flex;align-items:center;gap:6px;font-size:17px;color:var(--navy);margin-bottom:4px}
.foot-phone span{font-size:13px;color:var(--text)}
.foot-rule{position:absolute;left:153px;top:246px;width:894px;height:1px;background:var(--line)}
.copyright{position:absolute;left:153px;top:260px;font-size:11px;line-height:20px;color:var(--text)}
.socials{position:absolute;left:841px;top:268px;display:flex;gap:8px}
.socials span{width:28px;height:28px;border-radius:50%;display:block}
.bookmark{position:absolute;left:1130px;top:70px}
</style>
</head>
<body>

<header class="hero">
  <div class="hero-photo" role="img" aria-label="Photo of a modern multi-level renovated house at dusk"></div>
  <div class="hero-panel"></div>
  <div class="brand"><span class="brand-mark"></span>BRICKLINE GAINS</div>
  <nav class="main-nav"><span>Events</span><span>Media</span><span>Projects</span><span>Blog</span><span>eBooks</span></nav>
  <div class="ask">ASK A QUESTION
    <svg width="20" height="20" viewBox="0 0 20 20"><circle cx="10" cy="10" r="10" fill="var(--green)"/><path d="M7 5.5l2 2-1 1.2c.6 1.3 1.6 2.3 2.9 2.9l1.2-1 2 2-1.4 1.6c-3.4-.4-6.3-3.3-6.7-6.7z" fill="#fff"/></svg>
    <span class="num">1300 555 014</span></div>
  <div class="btn" style="left:962px;top:38px;width:158px;height:38px">Book my seat !</div>
  <svg class="play" width="56" height="56" viewBox="0 0 56 56"><circle cx="28" cy="28" r="25" fill="none" stroke="#fff" stroke-width="3"/><path d="M23 18l14 10-14 10z" fill="#fff"/></svg>
  <h1 class="hero-title">Renovating Property for Profit Workshop</h1>
  <div class="hero-meta">
    <svg width="11" height="11" viewBox="0 0 12 12"><circle cx="6" cy="6" r="5" fill="none" stroke="#c9d0e3" stroke-width="1.4"/><path d="M6 3v3l2 1" stroke="#c9d0e3" stroke-width="1.4" fill="none"/></svg>
    <span>2<sup>nd</sup> May 2017 &nbsp;|</span>
    <svg width="9" height="12" viewBox="0 0 9 12"><path d="M4.5 0A4.5 4.5 0 0 0 0 4.5C0 8 4.5 12 4.5 12S9 8 9 4.5A4.5 4.5 0 0 0 4.5 0z" fill="#c9d0e3"/><circle cx="4.5" cy="4.5" r="1.6" fill="var(--navy)"/></svg>
    <span>Harbourline Hotel Parramatta</span>
  </div>
  <p class="hero-tag">Make <em>more money in 12 weeks Renovating Property</em> than most people make in 12 months in a job!</p>
  <div class="hero-price">Tickets Only <b>$29.</b></div>
  <div class="btn" style="left:665px;top:462px;width:160px;height:35px">Book my seat!</div>
</header>

<section class="instructors">
  <div class="eyebrow" style="top:50px">Who we are</div>
  <h2 class="section-title" style="top:70px">Workshop Instructors</h2>

  <article class="instructor" style="left:158px">
    <div class="instructor-photo" role="img" aria-label="Portrait photo of instructor Reid Calloway"></div>
    <svg class="instructor-chart" width="110" height="90" viewBox="0 0 110 90"><rect x="10" y="50" width="14" height="30" fill="var(--orange)"/><rect x="30" y="36" width="14" height="44" fill="var(--orange)"/><rect x="50" y="22" width="14" height="58" fill="var(--orange)"/><rect x="70" y="8" width="14" height="72" fill="var(--orange)"/><path d="M2 82 L40 56 L58 66 L96 30" stroke="var(--navy)" stroke-width="6" fill="none"/><path d="M84 24 L104 20 L100 40z" fill="var(--navy)"/></svg>
    <div class="instructor-name">Reid Calloway:</div>
    <p class="instructor-bio">In 1984, at just 19 years old, I began investing in property. Over the course of the past 30 years, I've invested more than $250,000 in personal development, property seminars and programs with experts in their respective fields. Before launching Keystone Estate Learning with Owen, I was the CEO of a Brennan Hydraulic Company, and before that, ...</p>
    <div class="btn">More</div>
  </article>

  <article class="instructor two" style="left:613px">
    <div class="instructor-photo" role="img" aria-label="Portrait photo of instructor Owen Hartley-Vance"></div>
    <svg class="instructor-chart" width="110" height="90" viewBox="0 0 110 90"><rect x="10" y="50" width="14" height="30" fill="var(--orange)"/><rect x="30" y="36" width="14" height="44" fill="var(--orange)"/><rect x="50" y="22" width="14" height="58" fill="var(--orange)"/><rect x="70" y="8" width="14" height="72" fill="var(--orange)"/><path d="M2 82 L40 56 L58 66 L96 30" stroke="var(--navy)" stroke-width="6" fill="none"/><path d="M84 24 L104 20 L100 40z" fill="var(--navy)"/></svg>
    <div class="instructor-name">Owen Hartley-Vance:</div>
    <p class="instructor-bio">I began investing in property in 2005, when I was 25 years old. During the past 10 years, I have invested $100,000 in personal development and property seminar programs with the top people in the field of wealth creation. I consider property investment core to my continuous development as an individual AND as a businessperson. I also have an ASIC approved ...</p>
    <div class="btn">More</div>
  </article>
</section>

<section class="topics">
  <h2 class="section-title" style="top:46px">Workshop Topics</h2>
  <p class="topics-sub">Learn how to significantly increase your income and live an extraordinary life in this ground up fundamentals workshop.</p>
  <ul class="topic-list">
    <li class="topic"><span class="no">01.</span>Recent case studies of renovating for profit.<span class="toggle"></span></li>
    <li class="topic open"><span class="no">02.</span>Everybody can renovate, but can everybody renovate for profit?<span class="toggle"></span>
      <div class="topic-body">
        <p><b>Buying property on numbers, not on emotion:</b><br>How can I calculate profit, before spending a cent? How do I negotiate to make that profit? Why should I have a renovation strategy before even looking at a property.</p>
        <p><b>How to avoid costly mistakes:</b><br>How do I best manage the project effectively? What newbie mistakes do I need to watch out for? What can I do to ensure every dollar I spend generates a positive return?</p>
      </div>
    </li>
    <li class="topic"><span class="no">03.</span>Buying houses in any market and renovate for profit.<span class="toggle"></span></li>
    <li class="topic"><span class="no">04.</span>How to get funding for your project.<span class="toggle"></span></li>
    <li class="topic"><span class="no">05.</span>The proven property renovation step-by-step blueprint.<span class="toggle"></span></li>
    <li class="topic"><span class="no">06.</span>You'll receive the following finance &amp; property reports.<span class="toggle"></span></li>
    <li class="topic"><span class="no">07.</span>What will I learn?<span class="toggle"></span></li>
    <li class="topic"><span class="no">08.</span>Who is this workshop suitable for?<span class="toggle"></span></li>
    <li class="topic"><span class="no">09.</span>What are the requirements?<span class="toggle"></span></li>
  </ul>
</section>

<section class="stories">
  <div class="eyebrow" style="top:51px">Why us</div>
  <h2 class="section-title" style="top:70px">Latest Success Stories</h2>

  <svg class="carousel-arrow" style="left:100px" width="14" height="22" viewBox="0 0 14 22"><path d="M11 2L3 11l8 9" stroke="#9aa0ab" stroke-width="2.5" fill="none"/></svg>
  <svg class="carousel-arrow" style="left:1086px" width="14" height="22" viewBox="0 0 14 22"><path d="M3 2l8 9-8 9" stroke="#9aa0ab" stroke-width="2.5" fill="none"/></svg>

  <article class="story" style="left:156px">
    <div class="story-photo" role="img" aria-label="Photo of a renovated brick house in St Clair" style="background:linear-gradient(180deg,#9fc3e6 0%,#b9cfe0 40%,#a2745a 60%,#7b8a5a 100%)"></div>
    <div class="story-bar"><span class="story-place">St Clair NSW 2330</span>
      <div class="story-figs">BOUGHT: $370,000<br>SOLD: $445,000</div>
      <svg class="story-badge" width="94" height="94" viewBox="0 0 94 94"><circle cx="47" cy="47" r="46" fill="var(--orange)" stroke="#fff" stroke-width="2" stroke-dasharray="6 3"/><text x="47" y="46" text-anchor="middle" font-family="Lato,sans-serif" font-weight="900" font-size="17" fill="var(--navy)">$75,000</text><text x="47" y="62" text-anchor="middle" font-family="Lato,sans-serif" font-weight="700" font-size="10" fill="var(--navy)">PROFIT</text></svg>
    </div>
  </article>

  <article class="story" style="left:460px">
    <div class="story-photo" role="img" aria-label="Photo of a renovated red brick house in Werrington" style="background:linear-gradient(180deg,#8fb8e3 0%,#aac6e0 35%,#9a5a48 58%,#6e8a4e 100%)"></div>
    <div class="story-bar"><span class="story-place">Werrington NSW 2747</span>
      <div class="story-figs">BOUGHT: $345,000<br>SOLD: $465,000</div>
      <svg class="story-badge" width="94" height="94" viewBox="0 0 94 94"><circle cx="47" cy="47" r="46" fill="var(--orange)" stroke="#fff" stroke-width="2" stroke-dasharray="6 3"/><text x="47" y="46" text-anchor="middle" font-family="Lato,sans-serif" font-weight="900" font-size="16" fill="var(--navy)">$120,000</text><text x="47" y="62" text-anchor="middle" font-family="Lato,sans-serif" font-weight="700" font-size="10" fill="var(--navy)">PROFIT</text></svg>
    </div>
  </article>

  <article class="story" style="left:764px">
    <div class="story-photo" role="img" aria-label="Photo of a renovated house in Blackett" style="background:linear-gradient(180deg,#a9c9e8 0%,#c2d3e2 38%,#6e6660 58%,#5e7a44 100%)"></div>
    <div class="story-bar"><span class="story-place">Blackett NSW</span>
      <div class="story-figs">BOUGHT: $220,000<br>SOLD: $395,000</div>
      <svg class="story-badge" width="94" height="94" viewBox="0 0 94 94"><circle cx="47" cy="47" r="46" fill="var(--orange)" stroke="#fff" stroke-width="2" stroke-dasharray="6 3"/><text x="47" y="46" text-anchor="middle" font-family="Lato,sans-serif" font-weight="900" font-size="16" fill="var(--navy)">$175,000</text><text x="47" y="62" text-anchor="middle" font-family="Lato,sans-serif" font-weight="700" font-size="10" fill="var(--navy)">PROFIT</text></svg>
    </div>
  </article>

  <h2 class="people-title">What Our People Say</h2>
  <div class="avatar" role="img" aria-label="Photo of a workshop attendee" style="left:455px;top:486px;width:56px;height:56px;opacity:.8"></div>
  <div class="avatar" role="img" aria-label="Photo of workshop attendee Mark" style="left:551px;top:469px;width:98px;height:98px;border:3px solid var(--navy)"></div>
  <div class="avatar" role="img" aria-label="Photo of a workshop attendee" style="left:689px;top:486px;width:56px;height:56px;opacity:.8"></div>
  <p class="quote"><span class="mark">“</span> I would highly recommend people come to this event, the amount of information we have found out has been amazing! We felt very comfortable going through step by step how to renovate each phase and we were very happy with the contacts we made and the people we met. <span class="mark">”</span></p>
  <div class="quote-name">Mark &amp; Elise,</div>
  <div class="quote-date">10th November Workshop</div>
</section>

<section class="dates">
  <h2 class="dates-title">Workshop Dates &amp; Locations</h2>
  <table class="dates-table">
    <thead><tr>
      <th style="width:296px"><span class="th-in"><svg width="12" height="12" viewBox="0 0 12 12"><rect x="1" y="2" width="10" height="9" fill="none" stroke="#fff" stroke-width="1.4"/><path d="M1 5h10M4 0v3M8 0v3" stroke="#fff" stroke-width="1.4"/></svg>Date &amp; Time</span></th>
      <th style="width:296px"><span class="th-in"><svg width="9" height="12" viewBox="0 0 9 12"><path d="M4.5 0A4.5 4.5 0 0 0 0 4.5C0 8 4.5 12 4.5 12S9 8 9 4.5A4.5 4.5 0 0 0 4.5 0z" fill="#fff"/><circle cx="4.5" cy="4.5" r="1.6" fill="var(--navy)"/></svg>Location</span></th>
      <th><span class="th-in"><svg width="13" height="11" viewBox="0 0 13 11"><path d="M0 2h13v2.5a1.5 1.5 0 0 0 0 3V10H0V7.5a1.5 1.5 0 0 0 0-3z" fill="#fff"/></svg>Tickets Only</span></th>
    </tr></thead>
    <tbody><tr>
      <td>Tue 2<sup>nd</sup> May &nbsp;/ &nbsp;7-9pm</td>
      <td>Harbourline Parramatta<span class="map">&gt; View Map</span></td>
      <td class="price">$29</td>
    </tr></tbody>
  </table>
  <div class="btn" style="left:521px;top:245px;width:158px;height:36px">Book your seat</div>
</section>

<section class="ebook">
  <h2 class="ebook-title">EBook</h2>
  <p class="ebook-sub">by Australia's #1 Renovation Expert</p>
  <p class="ebook-note">ACCESS INSTANTLY to learn Marla's reno-success secrets</p>
  <div class="btn">Download now</div>
  <div class="cover" role="img" aria-label="Cover of the eBook 15 tips on renovating a bathroom" style="left:566px;top:128px;width:150px;height:194px;background:linear-gradient(180deg,#f3e4d8,#d9b9a3)"></div>
  <div class="cover" role="img" aria-label="Cover of the eBook 10 tips on how to renovate alfresco" style="left:900px;top:128px;width:150px;height:194px;background:linear-gradient(180deg,#3d7fc6,#9fc2e6 60%,#c8b49a)"></div>
  <div class="cover" role="img" aria-label="Cover of the eBook 60 insider tips on adding value to your property renovation" style="left:695px;top:64px;width:226px;height:290px;background:linear-gradient(180deg,#ffffff 0%,#f2f4f8 30%,#b08a68 60%,#e9e4dd 100%)"></div>
</section>

<footer class="site-footer">
  <div class="brand"><span class="brand-mark"></span>BRICKLINE GAINS</div>
  <div class="foot-col" style="left:384px"><h4>Quick Link</h4>
    <ul><li>Events</li><li>Media</li><li class="active">Projects</li><li>Testimonials</li><li>Blog</li><li>eBooks</li></ul></div>
  <div class="foot-col" style="left:610px"><h4>Help &amp; Support</h4>
    <ul><li>About Us</li><li>FAQ</li><li>Contact Us</li><li>Privacy</li><li>Disclaimer</li><li>Terms</li></ul></div>
  <div class="foot-col" style="left:839px"><h4>Ask Question</h4>
    <div class="foot-phone"><span>Call:</span><svg width="18" height="18" viewBox="0 0 20 20"><circle cx="10" cy="10" r="10" fill="var(--green)"/><path d="M7 5.5l2 2-1 1.2c.6 1.3 1.6 2.3 2.9 2.9l1.2-1 2 2-1.4 1.6c-3.4-.4-6.3-3.3-6.7-6.7z" fill="#fff"/></svg>1300 555 014</div>
    <div>info@bricklinegains.com.au</div>
    <h4 style="margin:10px 0 0">Find Us</h4>
    <div>P.O. Box 418, Kellyville<br>Sydney, Australia</div></div>
  <svg class="bookmark" width="18" height="28" viewBox="0 0 18 28"><path d="M2 2h14v24l-7-6-7 6z" fill="none" stroke="var(--ink)" stroke-width="2.5"/></svg>
  <div class="foot-rule"></div>
  <p class="copyright">© Copyright 2017 Keystone Estate Learning. All Rights Reserved.<br>ABN 42 118 660 907</p>
  <div class="socials"><span style="background:#3b5998"></span><span style="background:#1da1f2"></span><span style="background:#dd4b39"></span><span style="background:#0e76a8"></span><span style="background:#e62117"></span></div>
</footer>

</body>
</html>
```